Creative Stationary For Security Solutions Company
Halvern Guard Services
Creative Stationary For Security Solutions Company - Security
Creative Brief
Professional
Wesley Kolvasky
wesley@halvernguard.example
www.halvernguard.example
California PI No. 51928 And California PPO No. 40261
Logo has been uploaded in different color variations. Feel free to experiment, however I prefer the logo with black highlights on the visor, nose and neck (#1 I believe) I will provide my phone numbers towards the end of the project. Thanks and have fun.
I would like to see my logo on one side and info on the other. But feel free to experiment.

```html
<!DOCTYPE html>
<html lang="en">
<head>
<meta charset="utf-8">
<title>Halvern Guard Services – Business Card</title>
<link href="https://fonts.googleapis.com/css2?family=Montserrat:wght@800&family=Open+Sans:wght@400;600&display=swap" rel="stylesheet">
<style>
  :root {
    --orange: #f0922f;
    --orange-deep: #e9801c;
    --ink: #161616;
    --paper: #ffffff;
    --backdrop: #d9d9d9;
    --line: #ffffff;
  }
  * { box-sizing: border-box; margin: 0; padding: 0; }
  html, body { width: 1200px; height: 871px; overflow: hidden; }
  body { background: var(--backdrop); font-family: "Open Sans", Arial, sans-serif; position: relative; }

  .card {
    position: absolute; width: 600px; height: 343px;
    background: var(--paper); overflow: hidden;
    box-shadow: 0 6px 18px rgba(0,0,0,.18);
  }
  .card--front { left: 60px; top: 80px; }
  .card--back { left: 540px; top: 448px; }

  .wordmark { display: flex; align-items: center; gap: 12px; }
  .wordmark__dot { width: 46px; height: 46px; border-radius: 50%; background: var(--ink); flex: none; }
  .wordmark__name {
    font-family: "Montserrat", Arial, sans-serif; font-weight: 800;
    color: var(--ink); letter-spacing: -1px; line-height: 1;
  }
  .wordmark__tag { color: var(--orange-deep); font-weight: 400; letter-spacing: .5px; }

  /* front */
  .front-identity { position: absolute; left: 34px; top: 178px; }
  .front-identity .wordmark__name { font-size: 40px; }
  .front-identity .wordmark__tag { font-size: 15px; color: var(--ink); margin-top: 2px; }
  .front-identity .front-url { font-size: 12px; color: var(--orange-deep); margin-top: 4px; }
  .front-emblem {
    position: absolute; right: -70px; top: 20px; width: 330px; height: 330px;
    border-radius: 50%; background: var(--orange);
  }

  /* back */
  .back-header { position: absolute; left: 110px; top: 40px; }
  .back-header .wordmark__name { font-size: 44px; }
  .back-header .wordmark__tag { font-size: 14px; margin-top: 2px; }
  .back-wave { position: absolute; left: 0; top: 0; width: 600px; height: 343px; }

  .back-person { position: absolute; left: 0; top: 205px; width: 300px; text-align: right; padding-right: 24px; color: var(--paper); }
  .back-person__name { font-size: 20px; font-weight: 400; }
  .back-person__role { font-size: 15px; margin-top: 2px; }
  .back-person__license { font-size: 9.5px; margin-top: 14px; line-height: 1.5; }
  .back-divider { position: absolute; left: 300px; top: 200px; width: 1px; height: 118px; background: var(--line); }

  .contact-list { position: absolute; left: 318px; top: 204px; list-style: none; color: var(--paper); font-size: 12px; line-height: 22px; }
  .contact-list li { display: flex; align-items: center; gap: 8px; }
  .contact-list svg { width: 11px; height: 11px; fill: var(--paper); flex: none; }
</style>
</head>
<body>

<section class="card card--front" aria-label="Card front">
  <div class="front-emblem"></div>
  <div class="front-identity">
    <div class="wordmark__name">HALVERN</div>
    <div class="wordmark__tag">GUARD SERVICES</div>
    <div class="front-url">www.halvernguard.example</div>
  </div>
</section>

<section class="card card--back" aria-label="Card back">
  <svg class="back-wave" viewBox="0 0 600 343" aria-hidden="true">
    <path d="M0 196 C170 150 330 215 600 140 L600 343 L0 343 Z" fill="var(--ink)"/>
    <path d="M0 204 C170 160 330 224 600 150 L600 343 L0 343 Z" fill="var(--orange)"/>
  </svg>

  <div class="back-header wordmark">
    <span class="wordmark__dot"></span>
    <div>
      <div class="wordmark__name">HALVERN</div>
      <div class="wordmark__tag">GUARD SERVICES</div>
    </div>
  </div>

  <div class="back-person">
    <div class="back-person__name">Wesley Kolvasky</div>
    <div class="back-person__role">Founder</div>
    <div class="back-person__license">California PI No. 51928<br>California PPO No. 40261</div>
  </div>
  <div class="back-divider"></div>

  <ul class="contact-list">
    <li><svg viewBox="0 0 12 12"><path d="M2 1h3l1 3-2 1a7 7 0 0 0 3 3l1-2 3 1v3c-6 1-10-3-9-9z"/></svg>999-999-9999</li>
    <li><svg viewBox="0 0 12 12"><path d="M3 0h6v12H3z M4 1v9h4V1z"/></svg>999-999-9999</li>
    <li><svg viewBox="0 0 12 12"><path d="M1 4h10v6H1z M3 0h6v3H3z"/></svg>999-999-9999</li>
    <li><svg viewBox="0 0 12 12"><path d="M0 2h12v8H0z M1 3l5 4 5-4z" fill-rule="evenodd"/></svg>wesley@halvernguard.example</li>
    <li><svg viewBox="0 0 12 12"><circle cx="6" cy="6" r="6"/></svg>www.halvernguard.example</li>
  </ul>
</section>

</body>
</html>
```